Business Card Design

I would like a new business card design for an accounting firm that specializes in resolving clients tax problems. I want the card to give the impression that we are not your typical stodgy accounting firm, but at the same time we will get the job done.
Industry/Entity Type
Business
Contact Information for Business Card
Marcus T Kelbeck
Certified Public Accountant
27-08 63rd Avenue
Glenmere, NY 11092
Tel: (718) 555-0143
Fax: (888) 555-0176
e-mail: mtkledger@quillpost.net
website: harborstonefiscalaidgroup.com

```html
<!DOCTYPE html>
<html lang="en">
<head>
<meta charset="utf-8">
<title>Marcus T Kelbeck – Business Card</title>
<link rel="stylesheet" href="https://fonts.googleapis.com/css2?family=Cabin:wght@400;700&display=swap">
<style>
  :root {
    --navy: #12244b;
    --red: #d6212d;
    --white: #ffffff;
  }
  * { margin: 0; padding: 0; box-sizing: border-box; }
  html, body { width: 1200px; height: 702px; overflow: hidden; background: var(--navy); }
  .card {
    position: relative;
    width: 1200px;
    height: 702px;
    background: var(--navy);
    color: var(--white);
    font-family: "Cabin", "Gill Sans", sans-serif;
  }
  .card__name {
    position: absolute;
    top: 106px;
    left: 0;
    width: 1195px;
    text-align: center;
    font-size: 78px;
    font-weight: 700;
    line-height: 1;
    color: var(--red);
    letter-spacing: 0.5px;
  }
  .card__title {
    position: absolute;
    top: 223px;
    left: 0;
    width: 1195px;
    display: flex;
    justify-content: center;
    align-items: center;
    gap: 14px;
    font-size: 26px;
    line-height: 1;
  }
  .card__title-rule {
    width: 98px;
    height: 2px;
    background: var(--white);
  }
  .card__divider {
    position: absolute;
    top: 393px;
    left: 0;
    width: 1200px;
    height: 4px;
    background: var(--white);
  }
  .contact-list {
    position: absolute;
    top: 482px;
    left: 53px;
    list-style: none;
  }
  .contact-list__item {
    display: flex;
    align-items: center;
    height: 42px;
    font-size: 29px;
  }
  .contact-list__icon {
    width: 23px;
    height: 23px;
    margin-right: 12px;
    flex: none;
  }
  .address {
    position: absolute;
    top: 528px;
    left: 828px;
    display: flex;
    align-items: center;
    font-style: normal;
    font-size: 28px;
    line-height: 38px;
  }
  .address__pin {
    width: 24px;
    height: 42px;
    margin-right: 20px;
  }
</style>
</head>
<body>
<div class="card">
  <h1 class="card__name">Marcus T Kelbeck</h1>
  <p class="card__title">
    <span class="card__title-rule"></span>
    <span>Certified Public Accountant</span>
    <span class="card__title-rule"></span>
  </p>

  <div class="card__divider"></div>

  <ul class="contact-list">
    <li class="contact-list__item">
      <svg class="contact-list__icon" viewBox="0 0 24 24" aria-hidden="true">
        <rect width="24" height="24" rx="3" fill="var(--red)"/>
        <path d="M8 5c1 0 2 3 2 4s-1.5 1.3-1.3 2c.6 1.7 2.3 3.4 4 4 .7.2 1-1.3 2-1.3s4 1 4 2-1 3-3 3C10 18.7 5.3 14 5.3 8.3 5.3 6 7 5 8 5z" fill="var(--navy)"/>
      </svg>
      <span>718 555-0143</span>
    </li>
    <li class="contact-list__item">
      <svg class="contact-list__icon" viewBox="0 0 24 24" aria-hidden="true">
        <rect x="6" y="2" width="12" height="6" fill="var(--red)"/>
        <rect x="1" y="9" width="22" height="9" rx="2" fill="var(--red)"/>
        <rect x="6" y="15" width="12" height="7" fill="var(--red)" stroke="var(--navy)" stroke-width="1.5"/>
      </svg>
      <span>888 555-0176</span>
    </li>
    <li class="contact-list__item">
      <svg class="contact-list__icon" viewBox="0 0 24 24" aria-hidden="true">
        <rect x="1" y="5" width="22" height="15" fill="var(--red)"/>
        <path d="M1 5l11 9 11-9" fill="none" stroke="var(--navy)" stroke-width="1.8"/>
      </svg>
      <span>mtkledger@quillpost.net</span>
    </li>
    <li class="contact-list__item">
      <svg class="contact-list__icon" viewBox="0 0 24 24" aria-hidden="true">
        <circle cx="12" cy="12" r="11" fill="var(--red)"/>
        <g fill="none" stroke="var(--navy)" stroke-width="1.4">
          <ellipse cx="12" cy="12" rx="5" ry="11"/>
          <line x1="12" y1="1" x2="12" y2="23"/>
          <line x1="1" y1="12" x2="23" y2="12"/>
          <line x1="3" y1="7" x2="21" y2="7"/>
          <line x1="3" y1="17" x2="21" y2="17"/>
        </g>
      </svg>
      <span>harborstonefiscalaidgroup.com</span>
    </li>
  </ul>

  <address class="address">
    <svg class="address__pin" viewBox="0 0 24 42" aria-hidden="true">
      <path d="M12 0C5.4 0 0 5.4 0 12c0 9 12 30 12 30s12-21 12-30C24 5.4 18.6 0 12 0z" fill="var(--red)"/>
      <circle cx="12" cy="12" r="4.5" fill="var(--navy)"/>
    </svg>
    <span>27-08 63rd Avenue<br>Glenmere, NY 11092</span>
  </address>
</div>
</body>
</html>
```